Dalton Power Supply, Inc. Business Card Design

We are an Electrical Distributor looking for a Modern, Professional Business Card design.

Target Market(s)

Residential Commercial Industrial

Industry/Entity Type

Electrical

Contact Information for Business Card

Dalton Power Supply, Inc.
418 Maple Ridge Lane
Brookvale, NC 27514
555-214-7630
555-214-8842 Fax
daltonpower@brightmail-example.net

```html
<!DOCTYPE html>
<html lang="en">
<head>
<meta charset="utf-8">
<title>Dalton Power Supply, Inc. – Business Card</title>
<link rel="stylesheet" href="https://fonts.googleapis.com/css2?family=Open+Sans:wght@400;600;700&display=swap">
<style>
  :root {
    --bg: #ecebe8;
    --paper: #ffffff;
    --red: #ff1f00;
    --orange: #ff9200;
    --brand: #ff5a00;
    --ink-light: #ffffff;
  }
  html, body { margin: 0; padding: 0; overflow: hidden; }
  body { width: 1200px; height: 900px; background: var(--bg); font-family: "Open Sans", Arial, sans-serif; }
  .stage { position: relative; width: 1200px; height: 900px; }
  .card-shapes { position: absolute; inset: 0; }
  .front-text { position: absolute; left: 280px; top: 0; color: var(--ink-light); }
  .wordmark { position: absolute; margin: 0; font-weight: 600; line-height: 1; white-space: nowrap; }
  .wordmark .name-main { display: block; font-size: 36px; letter-spacing: 1px; }
  .wordmark .name-sub { display: block; font-size: 12.5px; letter-spacing: 3.6px; margin-top: 6px; }
  .front-wordmark { left: 285px; top: 140px; color: var(--ink-light); }
  .back-wordmark { left: 597px; top: 672px; color: var(--brand); text-align: center; }
  .back-wordmark .name-main { font-size: 40px; }
  .back-wordmark .name-sub { font-size: 13.5px; letter-spacing: 4px; }
  .holder-name { position: absolute; top: 211px; margin: 0; font-size: 21px; font-weight: 700; white-space: nowrap; }
  .address { position: absolute; top: 252px; margin: 0; font-style: normal; font-size: 14.5px; line-height: 20px; white-space: nowrap; }
  .contacts { position: absolute; top: 312px; margin: 0; padding: 0; list-style: none; font-size: 14.5px; line-height: 20px; white-space: nowrap; }
  .contacts li { display: flex; align-items: center; gap: 8px; }
  .contacts svg { width: 11px; height: 11px; fill: var(--ink-light); }
</style>
</head>
<body>
<div class="stage">
  <svg class="card-shapes" width="1200" height="900" viewBox="0 0 1200 900" aria-hidden="true">
    <defs>
      <linearGradient id="frontFill" x1="0" y1="0" x2="0" y2="1">
        <stop offset="0" stop-color="var(--red)"/>
        <stop offset="0.4" stop-color="var(--orange)"/>
        <stop offset="1" stop-color="var(--red)"/>
      </linearGradient>
    </defs>
    <rect class="front-card" x="238" y="62" width="555" height="343" fill="var(--paper)"/>
    <polygon class="front-face" fill="url(#frontFill)"
      points="238,62 793,62 793,150 765,235 735,215 705,290 682,278 663,405 238,405"/>
    <polygon class="back-card" fill="var(--paper)"
      points="458,518 1017,518 1017,860 562,860 548,745 510,770 492,700 458,720"/>
  </svg>

  <p class="wordmark front-wordmark">
    <span class="name-main">DALTON</span>
    <span class="name-sub">POWER SUPPLY, INC</span>
  </p>

  <div class="front-text">
    <h1 class="holder-name">DALTON</h1>
    <address class="address">418 Maple Ridge Lane<br>Brookvale, NC 27514</address>
    <ul class="contacts">
      <li><svg viewBox="0 0 12 12"><path d="M2.5 0.5l2 2.5-1 1.3c.7 1.5 1.7 2.5 3.2 3.2l1.3-1 2.5 2-1.2 2C5 10.5 1.5 7 0.5 2z"/></svg>555-214-7630</li>
      <li><svg viewBox="0 0 12 12"><path d="M3 0h5v3H3zM1 4h10v6H9v2H3v-2H1zM4 8v3h4V8z"/></svg>555-214-8842</li>
      <li><svg viewBox="0 0 12 12"><path d="M0 2h12v8H0zM1 3l5 4 5-4z" fill-rule="evenodd"/></svg>daltonpower@brightmail-example.net</li>
    </ul>
  </div>

  <p class="wordmark back-wordmark">
    <span class="name-main">DALTON</span>
    <span class="name-sub">POWER SUPPLY, INC</span>
  </p>
</div>
</body>
</html>
```